Verdanix gym flyer

Use the text offered in the word document and add the appropriate images in the space provided. The images may need to be resized.Can the font be bold and silver with a black outline.Can the background be light blue.I have submitted a design request for some business cards. I'd like the cards and the flyer to match.

Industry/Entity Type

Gym

```html
<!DOCTYPE html>
<html lang="en">
<head>
<meta charset="utf-8">
<title>Verdanix Body Transformation Cards</title>
<link href="https://fonts.googleapis.com/css2?family=Roboto+Condensed:ital,wght@0,400;0,700;1,700&family=Roboto:wght@300;700&display=swap" rel="stylesheet">
<style>
  :root {
    --page: #1f6a95;
    --card-light: #f2fafd;
    --card-mid: #bfe6f3;
    --card-deep: #4ec4e6;
    --facet: #2a8fd0;
    --facet-violet: #5a63c9;
    --ink: #111111;
    --silver: #f4f6f8;
    --frame: #2b2b2b;
    --photo-warm: #6d5a52;
    --photo-dark: #2c2623;
    --photo-green: #6f8a6a;
    --photo-skin: #b98f78;
  }
  * { box-sizing: border-box; margin: 0; padding: 0; }
  html, body { width: 1200px; height: 1200px; overflow: hidden; }
  body { background: var(--page); position: relative; font-family: "Roboto Condensed", sans-serif; color: var(--ink); }

  .card {
    position: absolute; width: 724px; height: 424px; overflow: hidden;
    background: linear-gradient(180deg, var(--card-deep) 0%, var(--card-mid) 30%, var(--card-light) 55%, var(--card-mid) 100%);
    box-shadow: 6px 8px 14px rgba(0,0,0,0.35);
  }
  .card--front { left: 256px; top: 162px; }
  .card--back { left: 246px; top: 635px; }
  .card__facets { position: absolute; inset: 0; width: 100%; height: 100%; }

  .card__text { position: absolute; left: 0; right: 0; text-align: center; white-space: nowrap; }

  .headline {
    top: 52px; font-size: 39px; line-height: 46px; font-weight: 700; letter-spacing: -0.5px;
    color: var(--silver);
    text-shadow:
      -2px 0 0 var(--ink), 2px 0 0 var(--ink), 0 -2px 0 var(--ink), 0 2px 0 var(--ink),
      -1.5px -1.5px 0 var(--ink), 1.5px -1.5px 0 var(--ink), -1.5px 1.5px 0 var(--ink), 1.5px 1.5px 0 var(--ink),
      0 3px 3px rgba(0,0,0,0.35);
  }
  .subhead {
    top: 106px; font-size: 25px; font-weight: 700; line-height: 30px; letter-spacing: -0.8px;
    color: var(--silver);
    text-shadow:
      -1.5px 0 0 var(--ink), 1.5px 0 0 var(--ink), 0 -1.5px 0 var(--ink), 0 1.5px 0 var(--ink),
      -1px -1px 0 var(--ink), 1px -1px 0 var(--ink), -1px 1px 0 var(--ink), 1px 1px 0 var(--ink);
  }
  .tagline { top: 312px; font-size: 27px; line-height: 32px; letter-spacing: -0.3px; }
  .tagline em { font-weight: 700; font-style: italic; }

  .result {
    position: absolute; width: 150px; height: 127px; display: flex;
    border: 2px solid var(--frame); background: var(--frame); gap: 2px;
  }
  .result__half { flex: 1; }
  .front-r1 { left: 201px; top: 180px; }
  .front-r2 { left: 362px; top: 180px; }
  .back-r1 { left: 216px; top: 53px; }
  .back-r2 { left: 377px; top: 53px; }
  .tone-warm { background: linear-gradient(160deg, var(--photo-warm), var(--photo-dark)); }
  .tone-dark { background: linear-gradient(180deg, var(--photo-skin) 0%, var(--photo-dark) 55%); }
  .tone-green { background: linear-gradient(180deg, var(--photo-green), var(--photo-skin) 60%, #8c8c8c); }
  .tone-pale { background: linear-gradient(180deg, #d9d2cb, var(--photo-skin) 55%, #3a3a3a); }

  .role-title { top: 190px; font-size: 38px; line-height: 44px; font-weight: 700; letter-spacing: -0.5px; }
  .offer { top: 236px; font-family: "Roboto", sans-serif; font-weight: 300; font-size: 26px; line-height: 31px; }
  .phone { top: 300px; font-family: "Roboto", sans-serif; font-weight: 700; font-size: 32px; line-height: 38px; }
  .social { top: 340px; font-family: "Roboto", sans-serif; font-weight: 700; font-size: 30px; line-height: 38px; }
</style>
</head>
<body>

<section class="card card--front">
  <svg class="card__facets" viewBox="0 0 724 424" preserveAspectRatio="none" aria-hidden="true">
    <polygon points="0,0 120,0 724,300 724,424 640,424 0,60" fill="var(--facet)" opacity="0.12"/>
    <polygon points="724,0 560,0 0,330 0,424 120,424 724,60" fill="var(--facet)" opacity="0.1"/>
    <polygon points="30,0 90,0 160,60" fill="var(--facet-violet)" opacity="0.5"/>
    <polygon points="620,0 724,0 724,20" fill="var(--facet-violet)" opacity="0.45"/>
    <polygon points="260,424 362,360 470,424" fill="var(--facet)" opacity="0.12"/>
  </svg>
  <p class="card__text headline">Are you happy with your body shape?</p>
  <p class="card__text subhead">Would you like to improve your health &amp; energy levels<br>at the same time as transforming your body shape?</p>
  <div class="result front-r1">
    <div class="result__half tone-warm" role="img" aria-label="Before photo of a female client"></div>
    <div class="result__half tone-warm" role="img" aria-label="After photo of the same client in a black dress"></div>
  </div>
  <div class="result front-r2">
    <div class="result__half tone-green" role="img" aria-label="Before photo of a male client outdoors"></div>
    <div class="result__half tone-green" role="img" aria-label="After photo of the same client, slimmer"></div>
  </div>
  <p class="card__text tagline">Get your body looking exactly how you<br>want it to look and more importantly... <em>KEEP IT THAT WAY</em></p>
</section>

<section class="card card--back">
  <svg class="card__facets" viewBox="0 0 724 424" preserveAspectRatio="none" aria-hidden="true">
    <polygon points="0,0 120,0 724,300 724,424 640,424 0,60" fill="var(--facet)" opacity="0.12"/>
    <polygon points="724,0 560,0 0,330 0,424 120,424 724,60" fill="var(--facet)" opacity="0.1"/>
    <polygon points="30,0 90,0 160,60" fill="var(--facet-violet)" opacity="0.5"/>
    <polygon points="620,0 724,0 724,20" fill="var(--facet-violet)" opacity="0.45"/>
    <polygon points="260,424 362,360 470,424" fill="var(--facet)" opacity="0.12"/>
  </svg>
  <div class="result back-r1">
    <div class="result__half tone-pale" role="img" aria-label="Before photo of a female client holding a baby"></div>
    <div class="result__half tone-dark" role="img" aria-label="After photo of the same client in black outfit"></div>
  </div>
  <div class="result back-r2">
    <div class="result__half tone-pale" role="img" aria-label="Before photo of a male client, shirtless"></div>
    <div class="result__half tone-pale" role="img" aria-label="After photo of the same client, leaner"></div>
  </div>
  <p class="card__text role-title">Wellness &amp; Body Transformation Coach</p>
  <p class="card__text offer">Call Callum for a FREE and unique body<br>evaluation tailored to YOU.</p>
  <p class="card__text phone">07700 900 418</p>
  <p class="card__text social">Social: Callum Hartley</p>
</section>

</body>
</html>
```